Lumora vale- referral cards for new customers

Hey,

I would like 1 set of business cards with the following details:

10% off any sales / coupon code
Our phone number: 4702938165
Menu :Lumoravale.example (for the menu)
A line left blank to hand write an activation code: either on top or just on one side

Include the Lumora Vale logo ( your choice of black or white logo)
This card is to drive orders for people to order a cannabis order with Lumora Vale. Please make the logo a large part of the card on both sides.

Target Market(s)

People who consume cannabis 21 and up

Industry/Entity Type

Business

Contact Information for Business Card

This business card will be given to customers so they can then give it to other customers and generate referalls. We need this card to be elegant, impressionable, professional, and something worth keeping and passing to friends.

Font styles to use
Decorative
Script

Colors
33a6d7
85acd3
3176b5
0455a3
0592cd
85cae6
cee9f5
eaf1f7
757575

Requirements
Must have
• Our website
• Phone Number
• The 10% off an order
• Spot for activation code
Nice to have
• Eye catching design
• Look classy
• Textured feel or textured look
Should not have
• Do not look super cannabis heady
• Do not look attractive to children

```html
<!DOCTYPE html>
<html lang="en">
<head>
<meta charset="utf-8">
<title>Lumora Vale – Referral Card</title>
<link rel="stylesheet" href="https://fonts.googleapis.com/css2?family=Lato:wght@400;700&display=swap">
<style>
  :root {
    --stage: #000000;
    --card-light: #ffffff;
    --olive: #575a26;
    --ink: #2a2a2a;
    --on-olive: #ffffff;
  }
  * { margin: 0; padding: 0; box-sizing: border-box; }
  html, body {
    width: 1200px; height: 900px; overflow: hidden;
    background: var(--stage);
    font-family: "Lato", Arial, sans-serif;
  }
  .stage { position: relative; width: 1200px; height: 900px; }

  .card { position: absolute; top: 275px; width: 477px; height: 294px; overflow: hidden; }
  .card--front {
    left: 116px; background: var(--card-light);
    border-radius: 0 48px 0 48px;
  }
  .card--back {
    left: 622px; background: var(--olive);
    border-radius: 48px 0 48px 0;
  }

  .activation {
    position: absolute; left: 27px; top: 40px;
    font-size: 13px; color: var(--ink); letter-spacing: 0.2px;
  }
  .offer {
    position: absolute; right: 27px; top: 44px; text-align: right; color: var(--olive);
    font-weight: 700;
  }
  .offer__amount { display: block; font-size: 28px; line-height: 1; }
  .offer__label { display: block; font-size: 15px; margin-top: 6px; }

  .contact-band { position: absolute; left: 0; top: 127px; width: 477px; height: 144px; }
  .contact {
    position: absolute; right: 28px; top: 193px; text-align: right;
    color: var(--on-olive); font-size: 20px; line-height: 28px;
  }
  .contact__row { display: flex; align-items: center; justify-content: flex-end; gap: 8px; }
  .contact__row svg { width: 13px; height: 13px; }

  .brand-mark {
    position: absolute; left: 8px; top: 130px; width: 180px; height: 150px;
    display: flex; align-items: center; justify-content: center;
    font-weight: 700; font-size: 20px; color: var(--olive); text-align: center;
  }

  .back-brand {
    position: absolute; left: 0; right: 0; top: 0; bottom: 0;
    display: flex; flex-direction: column; align-items: center; justify-content: center; gap: 18px;
  }
  .back-brand__dot { width: 120px; height: 120px; border-radius: 50%; background: rgba(255,255,255,0.12); }
  .back-brand__name { font-size: 30px; font-weight: 700; color: var(--on-olive); letter-spacing: 1px; }
</style>
</head>
<body>
<main class="stage">
  <section class="card card--front">
    <p class="activation">ACTIVATION CODE _______</p>
    <p class="offer"><span class="offer__amount">10% OFF</span><span class="offer__label">AN ORDER</span></p>

    <svg class="contact-band" viewBox="0 0 477 144" aria-hidden="true">
      <polygon points="170,0 477,0 477,144 185,144 178,72" fill="var(--olive)"/>
    </svg>

    <div class="brand-mark">Lumora Vale</div>

    <div class="contact">
      <div class="contact__row">4702938165
        <svg viewBox="0 0 24 24" aria-hidden="true"><path fill="#fff" d="M6.6 10.8a15 15 0 0 0 6.6 6.6l2.2-2.2a1 1 0 0 1 1-.25 11.4 11.4 0 0 0 3.6.57 1 1 0 0 1 1 1V20a1 1 0 0 1-1 1A17 17 0 0 1 3 4a1 1 0 0 1 1-1h3.5a1 1 0 0 1 1 1c0 1.25.2 2.45.57 3.57a1 1 0 0 1-.25 1z"/></svg>
      </div>
      <div class="contact__row">www.Lumoravale.example
        <svg viewBox="0 0 24 24" aria-hidden="true"><circle cx="12" cy="12" r="10" fill="#fff"/></svg>
      </div>
    </div>
  </section>

  <section class="card card--back">
    <div class="back-brand">
      <div class="back-brand__dot"></div>
      <div class="back-brand__name">Lumora Vale</div>
    </div>
  </section>
</main>
</body>
</html>
```